Dietitian/Nutritionist seeks trifold marketing brochure

We need a trifold brochure for marketing to patients within a doctors surgery. This will be a source of information for prospective patients, what they can expect and how to contact us. The brochure needs to have some key information such as a brief description of the services available, fees, locations of clinics and contact information. Our current brochure has been uploaded which has the information you need to complete this project. The files you provide will allow us to edit the information at a later date as pricing and services change.

Target Market(s)

Patients who have been referred to see a dietitian/nutritionist and people who are considering seeing a dietitian/nutritionist but haven't decided

Industry/Entity Type

Dietician

Font styles to use
Serif

Colors

Designer to choose colors to be used in the design.

Requirements
Must have
• My logo
• Verified clinical mealwise logo
• My website address and contact details
• Most of the information that is in my current brochure
• Locations/names of the four clinics
Nice to have
• Images that promote cooking, health and wellbeing

```html
<!DOCTYPE html>
<html lang="en">
<head>
<meta charset="utf-8">
<title>Harbourline Nutrition &amp; Dietetics – Trifold Brochure</title>
<link href="https://fonts.googleapis.com/css2?family=Roboto:wght@400;500;700&family=Dancing+Script:wght@700&display=swap" rel="stylesheet">
<style>
:root{
  --green:#5cb531;
  --blue:#1e4fa6;
  --grey-wave:#b9bcc2;
  --ink:#222;
  --paper:#fff;
  --badge:#f07a2a;
  --backdrop:#1c1c1c;
}
*{box-sizing:border-box;margin:0;padding:0}
html,body{width:800px;height:1200px;overflow:hidden;background:var(--backdrop)}
body{position:relative;font-family:"Roboto",Arial,sans-serif;color:var(--ink)}
.sheet{position:absolute;left:10px;width:780px;height:570px;background:var(--paper);overflow:hidden}
.sheet--outside{top:20px}
.sheet--inside{top:610px}
.sheet-art{position:absolute;inset:0}
.fold{position:absolute;top:0;bottom:0;width:1px;background:rgba(0,0,0,.08)}
.block{position:absolute}
.photo{position:absolute;border-radius:10px;border:3px solid #fff;box-shadow:0 1px 4px rgba(0,0,0,.35)}
.band-title{position:absolute;top:8px;color:#fff;font-weight:500;font-size:17px;text-align:center}
.assist-head{left:26px;top:10px;color:#fff;font-size:11px;line-height:14px;width:220px}
.service-list{left:28px;top:52px;width:230px;font-size:11px;line-height:12.5px;list-style:none}
.service-list>li{margin-bottom:5px;padding-left:14px;position:relative;font-weight:700}
.service-list>li::before,.service-list ul li::before{content:"";position:absolute;left:0;top:3px;width:7px;height:7px;border-radius:50%;border:1.5px solid #555}
.service-list ul{list-style:none;font-weight:400;margin-top:1px}
.service-list ul li{position:relative;padding-left:14px}
.service-list ul li::before{background:#777;border:none}
.service-list .light{font-weight:400}
.brand{position:absolute;display:flex;align-items:center;gap:8px;color:var(--blue);font-weight:500}
.brand-dot{width:26px;height:26px;border-radius:50%;background:var(--green);flex:none}
.brand-name{line-height:1.05}
.brand-name small{display:block;font-size:12px}
.contact{left:290px;top:214px;width:210px;text-align:center;font-size:11.5px}
.contact .person{font-weight:700;font-size:13px;letter-spacing:.3px}
.contact .role{font-size:10px;color:#444;margin-bottom:6px}
.contact .phones{font-size:13px;font-weight:500;display:flex;justify-content:center;gap:12px;align-items:center}
.contact .phones svg,.contact .mail svg{vertical-align:-2px}
.contact .mail{font-size:11px}
.badge{position:absolute;width:92px;height:38px;border-radius:6px;background:var(--badge);box-shadow:0 1px 3px rgba(0,0,0,.3);color:#fff;font-size:7.5px;line-height:8.5px;padding:6px 0 0 6px}
.badge::after{content:"";position:absolute;right:6px;top:5px;width:28px;height:28px;border-radius:50%;background:#fff}
.locations{left:300px;top:394px;width:210px;font-size:10.5px;line-height:12px}
.locations h3{font-size:12px;font-weight:500;text-align:center;margin-bottom:5px}
.locations ul{list-style:none}
.locations li{position:relative;padding-left:18px;margin-bottom:3px}
.locations li svg{position:absolute;left:0;top:2px}
.locations b{font-weight:500}
.web{left:270px;top:538px;width:250px;text-align:center;color:#fff;font-size:12.5px;font-weight:500}
.tagline{left:530px;top:412px;width:244px;text-align:center;font-family:"Dancing Script",cursive;color:var(--blue);font-size:15.5px;line-height:20.5px}
.copy{font-size:11px;line-height:13.5px;text-align:justify}
.fees h4{font-size:11px;font-weight:500;text-decoration:underline;margin:9px 0 4px}
.fees h4:first-child{margin-top:0}
.fees .sub{text-decoration:none;margin-bottom:1px}
.section-head{font-weight:500;font-size:11.5px;margin-bottom:6px}
</style>
</head>
<body>

<section class="sheet sheet--outside">
  <svg class="sheet-art" width="780" height="570" viewBox="0 0 780 570" aria-hidden="true">
    <path d="M0 0H780V30H260L255 60 0 38Z" fill="var(--green)"/>
    <path d="M264 362C350 366 440 308 523 258C620 208 700 198 780 192" stroke="var(--grey-wave)" stroke-width="6" fill="none"/>
    <path d="M0 305C90 335 180 368 264 372C350 376 440 320 523 272C620 220 700 210 780 205L780 216C700 222 620 232 523 284C440 332 350 384 264 382C180 380 90 350 0 319Z" fill="var(--green)"/>
    <path d="M0 345C90 370 180 390 264 388C350 386 440 340 523 295C620 250 700 240 780 230L780 400C700 405 620 400 523 345C440 362 350 392 264 396C170 398 80 420 0 415Z" fill="var(--blue)"/>
    <rect x="0" y="522" width="780" height="48" fill="var(--blue)"/>
  </svg>
  <div class="fold" style="left:260px"></div>
  <div class="fold" style="left:520px"></div>

  <p class="block assist-head">Verified clinical mealwise can assist you with:</p>
  <ul class="block service-list">
    <li>Diabetes<ul><li>Impaired Glucose Tolerance</li><li>Type 1 and 2 Diabetes</li><li>Gestational Diabetes</li></ul></li>
    <li>Digestive Health<ul><li>Irritable Bowel Syndrome</li><li>Coeliac Disease</li><li>Diverticular Disease</li></ul></li>
    <li>Gastric Banding <span class="light">and other surgical methods of weight loss</span></li>
    <li>Cardiovascular<ul><li>High Cholesterol</li><li>High Blood Pressure</li><li>Risk Reduction</li></ul></li>
    <li>Weight Management<ul><li>Loss/Gain and Support</li></ul></li>
    <li>General Healthy Eating and Nutrition</li>
  </ul>
  <div class="photo" role="img" aria-label="Photo of grilled chicken with fresh salad" style="left:22px;top:426px;width:222px;height:118px;background:linear-gradient(135deg,#d9a873,#c4452f 45%,#5a9a3a 80%,#e9e2d0)"></div>

  <div class="photo" role="img" aria-label="Photo of fresh fruit, vegetables and a glass of milk" style="left:290px;top:20px;width:212px;height:116px;background:linear-gradient(120deg,#b98a4f,#e24a2b 40%,#f1eee6 55%,#c7372c 75%,#6a9b3a)"></div>
  <div class="brand" style="left:302px;top:160px;font-size:24px">
    <span class="brand-dot"></span>
    <span class="brand-name">Harbourline<small>Nutrition &amp; Dietetics</small></span>
  </div>
  <div class="block contact">
    <p class="person">DANIEL WHITCOMBE</p>
    <p class="role">Verified clinical mealwise &amp; Chef</p>
    <p class="phones">
      <span><svg width="13" height="11" viewBox="0 0 13 11"><path d="M1 4C1 1 12 1 12 4L10 5 9 3H4L3 5Z M3 6H10L11 10H2Z" fill="#333"/></svg> 041 555 203</span>
      <span><svg width="12" height="11" viewBox="0 0 12 11"><rect x="1" y="3" width="10" height="7" fill="none" stroke="#333"/><rect x="3" y="0.5" width="6" height="3" fill="none" stroke="#333"/></svg> 5550 1842</span>
    </p>
    <p class="mail"><svg width="11" height="8" viewBox="0 0 11 8"><rect x=".5" y=".5" width="10" height="7" fill="none" stroke="#333"/><path d="M.5 .5 5.5 4.5 10.5 .5" fill="none" stroke="#333"/></svg> daniel.w.nutrition@example.com</p>
  </div>
  <div class="badge" style="left:290px;top:292px">Verified<br>clinical<br>mealwise</div>
  <div class="block locations">
    <h3><svg width="8" height="11" viewBox="0 0 8 11"><path d="M4 0.5A3.5 3.5 0 0 1 7.5 4C7.5 6.5 4 10.5 4 10.5S.5 6.5 .5 4A3.5 3.5 0 0 1 4 .5Z" fill="none" stroke="#333"/></svg> LOCATIONS</h3>
    <ul>
      <li><svg width="12" height="9" viewBox="0 0 12 9"><path d="M1 1 11 4.5 1 8 4 4.5Z" fill="none" stroke="#333"/></svg><b>Hillcrest Medical Centre</b><br>Eastvale - Fridays</li>
      <li><svg width="12" height="9" viewBox="0 0 12 9"><path d="M1 1 11 4.5 1 8 4 4.5Z" fill="none" stroke="#333"/></svg><b>Linwood Medical</b><br>Wednesdays</li>
      <li><svg width="12" height="9" viewBox="0 0 12 9"><path d="M1 1 11 4.5 1 8 4 4.5Z" fill="none" stroke="#333"/></svg><b>Southbank Health Riverside</b><br>Thursdays</li>
      <li><svg width="12" height="9" viewBox="0 0 12 9"><path d="M1 1 11 4.5 1 8 4 4.5Z" fill="none" stroke="#333"/></svg><b>Millbrook Doctors Surgery</b><br>Approximately every 4 weeks</li>
    </ul>
  </div>
  <p class="block web">&#127760;&#xFE0E; www.riverbankdietitian.com.au</p>

  <div class="brand" style="left:555px;top:64px;font-size:30px">
    <span class="brand-dot"></span>
    <span class="brand-name">Harbourline<small style="font-size:14px">Nutrition &amp; Dietetics</small></span>
  </div>
  <div class="photo" role="img" aria-label="Photo of a tomato, feta and herb salad" style="left:548px;top:140px;width:218px;height:262px;background:radial-gradient(circle at 50% 45%,#e5483a,#c2331f 45%,#7c9b3c 75%,#eef0ec)"></div>
  <p class="block tagline">Helping you to meet your individual nutrition goals with an emphasis on practical skills, everyday foods, and providing you with up-to-date advice.</p>
</section>

<section class="sheet sheet--inside">
  <svg class="sheet-art" width="780" height="570" viewBox="0 0 780 570" aria-hidden="true">
    <rect x="0" y="0" width="780" height="40" fill="var(--green)"/>
    <path d="M0 262C130 250 270 270 380 296C500 322 640 322 780 296L780 308C640 336 500 338 380 310C270 284 130 270 0 276Z" fill="var(--grey-wave)"/>
    <path d="M0 305C130 290 270 305 380 330C500 355 640 352 780 322L780 336C640 366 500 372 380 345C270 320 130 306 0 318Z" fill="var(--green)"/>
    <path d="M200 345C300 350 400 370 523 385C640 395 720 380 780 360L780 405C700 415 620 410 523 400C420 388 320 365 200 345Z" fill="var(--blue)"/>
    <rect x="0" y="538" width="780" height="32" fill="var(--blue)"/>
  </svg>
  <div class="fold" style="left:260px"></div>
  <div class="fold" style="left:520px"></div>

  <h2 class="band-title" style="left:0;width:260px">Who We Are</h2>
  <p class="block copy" style="left:26px;top:62px;width:222px"><b style="font-weight:500">Verified clinical mealwise (VCMs)</b> are university trained experts in food and nutrition, they are able to translate the latest scientific evidence into sensible and practical advice. Dietitians differ from nutritionists as they have specific training in clinical environments such as hospitals. This training allows a dietitian to interpret blood tests, understand any food and medication interactions, and communicate with other health professionals involved in your care.</p>
  <p class="block copy" style="left:22px;top:372px;width:224px"><b style="font-weight:500">Seeing a dietitian for the first time</b> involves working with you to develop strategies and goals to improve your health. Follow-up visits are recommended to monitor your progress and may include more measurements and new strategies to help YOU realize your goals. Every person is unique and I can provide support and advice to suit your individual circumstances and lifestyle.</p>

  <div class="photo" role="img" aria-label="Photo of a smiling woman holding a bowl of fresh salad" style="left:290px;top:28px;width:218px;height:162px;background:linear-gradient(120deg,#e8e4dc,#d9a27a 40%,#a8542e 60%,#6aa13d 85%)"></div>
  <p class="block copy" style="left:292px;top:212px;width:216px">We work together to develop personalized eating plans that take into consideration your food preferences, health, work, family and lifestyle needs.</p>
  <div class="badge" style="left:410px;top:280px;height:44px">Verified<br>clinical<br>mealwise</div>
  <div class="block" role="img" aria-label="Photo of fresh strawberries in a round frame" style="left:300px;top:302px;width:84px;height:84px;border-radius:50%;border:4px solid #fff;box-shadow:0 1px 4px rgba(0,0,0,.35);background:radial-gradient(circle at 45% 55%,#e5393a,#b51f24 55%,#4d8f2f)"></div>
  <div class="block copy" style="left:292px;top:402px;width:218px">
    <p class="section-head">Individual &amp; Group Nutrition Counseling</p>
    <p>My unique set of skills allows me to work with individuals or small groups to achieve their health and nutrition goals. Together we create an individually tailored plan to help you achieve your goals whilst taking into account your family, work, and lifestyle commitments.</p>
  </div>

  <h2 class="band-title" style="left:520px;width:260px">Fees</h2>
  <div class="block copy fees" style="left:552px;top:56px;width:214px">
    <h4>Chronic Disease Management Plans</h4>
    <p>If your Doctor has referred you with a Chronic Disease Management Plan to assist in the ongoing management of your health condition, you are eligible for a rebate of $52.95 from Healthcover.</p>
    <h4>All Fees are Payable on the Day of Your Consultation</h4>
    <h4 class="sub">Private Patients</h4>
    <p style="text-align:left">Initial Consultation: <b style="font-weight:500">$120 (60 mins)</b><br>Follow-up Consultation: <b style="font-weight:500">$65 (30 mins)</b></p>
    <h4>Private Health Funds</h4>
    <p>Rebates are available through most private health funds but rates vary depending on your level of cover. Check with your fund directly to find out more.</p>
  </div>
  <div class="photo" role="img" aria-label="Photo of citrus fruit, kiwifruit, juice and a stethoscope" style="left:548px;top:420px;width:218px;height:116px;background:linear-gradient(120deg,#f4b942,#f08a24 40%,#7fae3a 70%,#f2f0ea)"></div>
</section>

</body>
</html>
```